Exhibition Stand Design for innovative Social Business

We are an innovative social business empowering people to value nature through ZUN, a complementary digital currency. We have attached the TEK_ZUN branding document, and are needing a design for our exhibition stand (https://fairbuildlab.com/produit/stand-parapluie-classic-pvc-3x4c/. The attached doc mocks up a stand on page 32, though we would like some messaging included, in line with our website www.tekzun.ch. You will see there how the branding concept has been implemented with the TEK:GROW, SHARE, THRIVE wording, as well as Everyone wins. Our green colours are included in the branding document. Many thanks!

Industry/Entity Type

Environment

Font styles to use
Other font styles liked:
• As per our attached fonts

Requirements
Must have
• Our attached branding guidelines gives our look and feel - Innovative / Dynamic / Vibrant / Reliable / Accessible / Connected.

```html
<!DOCTYPE html>
<html lang="en">
<head>
<meta charset="utf-8">
<title>TEK ZUN – Everyone wins</title>
<link href="https://fonts.googleapis.com/css2?family=Montserrat:wght@600;700&display=swap" rel="stylesheet">
<style>
  :root {
    --teal: #5fe6b4;
    --green: #42ec78;
    --lime: #1fe23c;
    --ink: #0c0c0c;
    --white: #ffffff;
    --panel: rgba(28, 96, 54, 0.62);
    --accent: #48e89a;
    --circle: rgba(225, 255, 230, 0.42);
  }
  * { margin: 0; padding: 0; box-sizing: border-box; }
  html, body { width: 1200px; height: 900px; overflow: hidden; background: #ffffff; }
  .stand-graphic {
    position: relative;
    width: 1200px;
    height: 900px;
    overflow: hidden;
    font-family: "Montserrat", sans-serif;
  }
  .landscape {
    position: absolute;
    inset: 0;
    background:
      linear-gradient(180deg, rgba(255,255,255,0.10) 0%, rgba(0,0,0,0) 35%, rgba(0,60,20,0.10) 100%),
      linear-gradient(120deg, var(--teal) 0%, var(--green) 45%, var(--lime) 100%);
  }
  .deco-circles { position: absolute; inset: 0; }
  .brand-name {
    position: absolute;
    left: 118px;
    top: 112px;
    font-size: 110px;
    font-weight: 700;
    line-height: 1;
    color: var(--ink);
  }
  .tagline {
    position: absolute;
    left: 330px;
    top: 252px;
    font-size: 64px;
    font-weight: 600;
    color: var(--white);
    line-height: 1;
  }
  .pillars {
    position: absolute;
    left: 121px;
    top: 360px;
    width: 468px;
    height: 460px;
    border-radius: 14px;
    background: var(--panel);
    padding: 33px 0 0 43px;
  }
  .pillars-heading {
    font-size: 84px;
    font-weight: 600;
    line-height: 1;
    color: var(--accent);
    margin-bottom: 2px;
  }
  .pillars-list { list-style: none; }
  .pillars-list li {
    font-size: 98px;
    font-weight: 600;
    line-height: 103px;
    color: var(--white);
  }
</style>
</head>
<body>
  <main class="stand-graphic">
    <div class="landscape" role="img" aria-label="Soft rolling green hills landscape tinted in green"></div>

    <svg class="deco-circles" width="1200" height="900" viewBox="0 0 1200 900" aria-hidden="true">
      <circle cx="1090" cy="136" r="266" fill="var(--circle)"/>
      <circle cx="1190" cy="892" r="236" fill="var(--circle)" opacity="0.75"/>
      <circle cx="0" cy="900" r="122" fill="var(--circle)" opacity="0.7"/>
    </svg>

    <h1 class="brand-name">TEK ZUN</h1>
    <p class="tagline">everyone wins</p>

    <section class="pillars">
      <p class="pillars-heading">TEK</p>
      <ul class="pillars-list">
        <li>GROW</li>
        <li>SHARE</li>
        <li>THRIVE</li>
      </ul>
    </section>
  </main>
</body>
</html>
```